Glow Up by Lakeside 21 day Challenge

We are having a Glow Up by Lakeside Challenge at our fitness studio. We need a poster design using the template attached as a reference. I have also included our Bromalux logo to put on the poster. Please DO NOT use the graphics in the flyer as we are expecting something much better :-)

-Size needed 11x17 with bleeding for printing

-We need this made in Photoshop (CS3 friendly) or at least delivered in PS as we might change some text or re-arrange the design later on.

-We need this in layers.

```html
<!DOCTYPE html>
<html lang="en">
<head>
<meta charset="utf-8">
<title>Glow Up by Lakeside 21 day Challenge – Bromalux Bootcamps</title>
<link rel="stylesheet" href="https://fonts.googleapis.com/css2?family=Titan+One&family=Anton&family=Oswald:wght@500;700&display=swap">
<style>
  :root {
    --sun-core: #fff6b8;
    --sun-mid: #ffc93a;
    --sun-edge: #f08a12;
    --sun-deep: #d9600a;
    --palm: #8a3d08;
    --ink: #13213f;
    --navy: #16264a;
    --banner-red: #e8531a;
    --gold: #ffd21f;
    --white: #ffffff;
    --pink: #ff3fa4;
    --violet: #7b3fe0;
    --sky: #3fb6ff;
    --alert: #c8141e;
    --brand-ink: #4a2308;
  }
  * { box-sizing: border-box; margin: 0; padding: 0; }
  html, body { width: 783px; height: 1200px; overflow: hidden; }
  body { font-family: "Oswald", sans-serif; background: var(--sun-edge); }

  .poster {
    position: relative;
    width: 783px;
    height: 1200px;
    overflow: hidden;
    background: radial-gradient(ellipse at 50% 38%, var(--sun-core) 0%, var(--sun-mid) 32%, var(--sun-edge) 70%, var(--sun-deep) 100%);
  }

  .palm {
    position: absolute;
    background: radial-gradient(ellipse at center, rgba(138,61,8,0.55) 0%, rgba(138,61,8,0.25) 50%, rgba(138,61,8,0) 72%);
  }
  .palm--top-left { left: -120px; top: -90px; width: 380px; height: 320px; }
  .palm--top-right { right: -130px; top: -70px; width: 360px; height: 300px; }
  .palm--bottom-left { left: -140px; bottom: -110px; width: 420px; height: 360px; }
  .palm--bottom-right { right: -150px; bottom: -120px; width: 440px; height: 380px; }

  .brand {
    position: absolute;
    left: 0; right: 0; top: 40px;
    display: flex; justify-content: center; align-items: center; gap: 14px;
  }
  .brand__mark { width: 26px; height: 26px; background: var(--brand-ink); }
  .brand__name {
    font-family: "Titan One", sans-serif;
    font-size: 58px;
    letter-spacing: 2px;
    color: var(--brand-ink);
  }

  .headline { position: absolute; left: 0; right: 0; top: 145px; text-align: center; font-family: "Titan One", sans-serif; }
  .headline__lead {
    display: block;
    font-size: 62px;
    line-height: 1;
    color: var(--white);
    text-shadow: 0 4px 0 var(--pink), 0 7px 0 var(--violet), 0 10px 14px rgba(0,0,0,0.3);
  }
  .headline__main {
    display: block;
    margin-top: 30px;
    font-size: 150px;
    line-height: 1;
    letter-spacing: -3px;
    background: linear-gradient(180deg, var(--sky) 0%, var(--pink) 50%, var(--violet) 100%);
    -webkit-background-clip: text; background-clip: text;
    color: transparent;
    filter: drop-shadow(0 6px 0 var(--navy)) drop-shadow(0 10px 10px rgba(0,0,0,0.3));
  }

  .banner {
    position: absolute;
    left: 50%; transform: translateX(-50%);
    text-align: center; white-space: nowrap;
    font-family: "Anton", sans-serif;
    color: var(--white);
  }
  .banner--dark { top: 470px; width: 400px; height: 52px; line-height: 52px; font-size: 30px; background: var(--navy); border-radius: 6px; letter-spacing: 0.5px; }
  .banner--bright { top: 532px; width: 580px; height: 66px; line-height: 66px; font-size: 38px; background: var(--banner-red); border: 3px solid var(--navy); border-radius: 6px; }

  .benefits { position: absolute; left: 108px; top: 668px; width: 360px; list-style: none; }
  .benefits li {
    position: relative; padding-left: 20px; margin-bottom: 6px;
    font-weight: 700; font-size: 17px; line-height: 1.15; color: var(--ink);
  }
  .benefits li::before { content: ""; position: absolute; left: 0; top: 6px; width: 10px; height: 10px; background: var(--gold); border: 1px solid var(--navy); }

  .offer {
    position: absolute; left: 480px; top: 682px; width: 212px; height: 150px;
    background: var(--navy); border: 3px solid var(--gold); border-radius: 14px;
    display: flex; flex-direction: column; justify-content: center; align-items: center;
    font-family: "Anton", sans-serif; color: var(--gold); text-align: center; line-height: 1.12;
  }
  .offer__value { font-size: 27px; }
  .offer__price { font-size: 32px; margin-top: 8px; }

  .testimonial { position: absolute; left: 0; right: 0; top: 862px; text-align: center; color: var(--ink); }
  .testimonial__label { font-weight: 700; font-size: 17px; }
  .testimonial__quote { font-weight: 500; font-style: italic; font-size: 17px; margin-top: 4px; }

  .cta { position: absolute; left: 0; right: 0; top: 928px; text-align: center; font-weight: 700; color: var(--alert); font-size: 21px; line-height: 1.2; }
</style>
</head>
<body>
<main class="poster">
  <div class="palm palm--top-left" role="img" aria-label="Palm tree fronds in the corner"></div>
  <div class="palm palm--top-right" role="img" aria-label="Palm tree fronds in the corner"></div>
  <div class="palm palm--bottom-left" role="img" aria-label="Palm tree and beach foliage"></div>
  <div class="palm palm--bottom-right" role="img" aria-label="Palm tree and beach foliage"></div>

  <header class="brand">
    <span class="brand__mark"></span>
    <span class="brand__name">BROMALUX</span>
  </header>

  <h1 class="headline">
    <span class="headline__lead">GLOW UP BY</span>
    <span class="headline__main">LAKESIDE</span>
  </h1>

  <div class="banner banner--dark">DISCOVER THE SECRET TO A</div>
  <div class="banner banner--bright">BEACH-READY BODY IN JUST 21 DAYS!</div>

  <ul class="benefits">
    <li>9 total training sessions designed to incinerate fat off your midsection, thighs, and arms</li>
    <li>21 days of nutritional guidance, including delicious recipes</li>
    <li>A Success Session to map out your individual plan for success</li>
    <li>Your very own Personal Accountability Coach to ensure you get results</li>
  </ul>

  <aside class="offer">
    <span class="offer__value">YOU GET ALL THIS<br>A $399 VALUE</span>
    <span class="offer__price">FOR ONLY $99!</span>
  </aside>

  <section class="testimonial">
    <p class="testimonial__label">INSERT TESTIMONIAL</p>
    <p class="testimonial__quote">I'VE NEVER BEEN MORE FIT IN MY LIFE—AT AGE 41! —MARISOL BRENNAN</p>
  </section>

  <p class="cta">HURRY! SPACE IS LIMITED TO ONLY 20 PARTICIPANTS!!!<br>CLAIM YOUR SPOT NOW: WEBSITE AND PHONE NUMBER</p>
</main>
</body>
</html>
```